Automotive Locksmiith company needs a website design and mobile website

We need a website design and a mobile design for an automotive locksmith company called Halvern Keyworks LLC.We are based in the center of the Dallas-Fort Worth Metroplex. We have a website that was directed more towards the towing services we also offer. We would like to have it more towards our locksmith products. Our main services include:
Auto keys duplication
Cutting of new car keys
Car Lockouts
Laser key replacement
Cutting keys by code
Broken key extractions
Production of transponder keys
Key fob programming
Door lock repairs
Ignition repairs/replacement
We work on 95% of the automotive market that includes Vorla, Tessin, QRT, Pembrook, Marquenne, Dunmoral, Brask, VX, Sorvalo, Kelto, Zephrane, Oru, Hadley, Norax, Tabori, Valdrenne, Quillon, Pipo, Runel Okarawe , Brevik, Solumé, Drennhofer, Kestra.
We are one of the most affordable services in the DFW area . Our prices for transponder copies start at $35 per key. We provide services for high-end vehicles also as QRT and Valdrenne. We can program the new proximity keys for Tabori Vehicles 2013-up. We also work on the new Pell Vehicles 20-13 and up including the Pell Arden head remote key.
We would like to have a similar style to the website we already have with the option to schedule an appointment on the mobile website. This mobile application will deliver an email when a new customer is requiring the service. It will ask for Year, Make, Model , Service to be performed( Key copy, Lockout, Lost Key, Change Ignition lock, change door lock, Other services.) Description of the service to be performed, Address, Select time of service.
Our current website is halvernkeyworks.example

Reason: Need pictures of webpages inside design (about us , location etc) and mobile pictures( how website looks in Quorra / android)

Automotive

• check word attachment

```html
<!DOCTYPE html>
<html lang="en">
<head>
<meta charset="utf-8">
<title>Halvern Keyworks LLC</title>
<link href="https://fonts.googleapis.com/css2?family=Lato:wght@700&family=Open+Sans:wght@400;600;700&display=swap" rel="stylesheet">
<style>
  :root {
    --brand: #12b5dc;
    --brand-deep: #0aa2c0;
    --ink: #1c1c1c;
    --slate: #3d5a6a;
    --muted: #7a8086;
    --pill: #cdeef7;
    --pill-strong: #aee7f5;
    --panel: #f2fafd;
    --line: #c9ccd0;
    --white: #ffffff;
  }
  * { box-sizing: border-box; margin: 0; padding: 0; }
  html, body { width: 1200px; height: 2557px; overflow: hidden; }
  body {
    position: relative;
    background: var(--white);
    font-family: "Open Sans", Arial, sans-serif;
    color: var(--ink);
  }
  .abs { position: absolute; }

  /* Header */
  .brand { left: 111px; top: 22px; display: flex; flex-direction: column; align-items: flex-start; }
  .brand-mark { width: 38px; height: 38px; background: var(--brand); margin-left: 120px; margin-bottom: 10px; }
  .brand-name { font-size: 26px; font-weight: 700; color: var(--slate); letter-spacing: -0.3px; white-space: nowrap; }
  .home-btn {
    left: 653px; top: 20px; width: 123px; height: 36px; background: var(--pill);
    display: flex; align-items: center; justify-content: center; gap: 10px;
    font-weight: 700; font-size: 20px; color: var(--brand);
  }
  .search {
    left: 789px; top: 20px; width: 301px; height: 36px; background: #d6e4e8;
    display: flex; align-items: center;
  }
  .search span { flex: 1; padding-left: 14px; font-size: 18px; color: #8a9aa0; }
  .search .go { width: 50px; height: 36px; background: #13788f; display: flex; align-items: center; justify-content: center; }
  .nav { left: 0; top: 92px; width: 1200px; height: 30px; font-size: 20px; color: var(--slate); }
  .nav-item { position: absolute; top: 0; color: inherit; text-decoration: none; white-space: nowrap; }

  /* Hero */
  .hero {
    left: 0; top: 133px; width: 1200px; height: 554px;
    background: linear-gradient(180deg, #f4f6f9 0%, #e9edf2 60%, #f6f7f9 100%);
    box-shadow: 0 10px 18px rgba(0,0,0,0.12);
  }
  .hero-art {
    left: 40px; top: 12px; width: 540px; height: 520px;
    background: linear-gradient(160deg, #5a5d62 0%, #3a3c40 40%, #c9a440 75%, #e6e9ee 100%);
    opacity: 0.85;
  }
  .hero-copy {
    left: 478px; top: 112px; width: 640px; text-align: center;
    font-family: "Lato", "Open Sans", sans-serif;
    font-size: 32px; font-weight: 700; line-height: 42px; color: var(--ink);
    white-space: nowrap;
  }
  .hero-copy .accent { color: var(--brand); font-size: 37px; }
  .hero-cta {
    left: 699px; top: 312px; width: 195px; height: 58px; border: 2px solid var(--brand);
    background: var(--white); color: var(--brand); font-size: 30px; font-weight: 600;
    display: flex; align-items: center; justify-content: center;
  }
  .dots { left: 975px; top: 503px; display: flex; gap: 13px; }
  .dots i { width: 20px; height: 20px; border-radius: 50%; background: #111; display: block; }
  .dots i.on { background: var(--brand); }

  /* Section headings */
  .sec-head { display: flex; align-items: center; height: 82px; }
  .sec-head .badge {
    width: 82px; height: 82px; border-radius: 50%; background: var(--pill);
    display: flex; align-items: center; justify-content: center; position: relative; z-index: 2;
  }
  .sec-head .label {
    height: 60px; margin-left: -22px; padding: 0 22px 0 36px; background: var(--pill);
    font-size: 30px; font-weight: 700; color: var(--ink); display: flex; align-items: center;
    box-shadow: 3px 3px 6px rgba(0,0,0,0.12);
  }

  /* About */
  .about-text {
    left: 111px; top: 844px; width: 590px; font-size: 14.5px; line-height: 24.8px; color: #333;
  }
  .btn {
    background: var(--pill-strong); color: var(--ink); font-weight: 600;
    display: flex; align-items: center; justify-content: center;
    box-shadow: 2px 3px 5px rgba(0,0,0,0.15);
  }
  .read-more { left: 542px; top: 1067px; width: 155px; height: 46px; font-size: 23px; }
  .feature {
    left: 789px; width: 299px; height: 102px;
    background: linear-gradient(90deg, #e3f3f8, #ffffff 70%);
    border: 1px solid #cfd8dc; box-shadow: 3px 4px 8px rgba(0,0,0,0.14);
    display: flex; align-items: center;
  }
  .feature .ico { width: 100px; display: flex; justify-content: center; }
  .feature .txt { flex: 1; text-align: center; font-size: 22px; font-weight: 700; line-height: 32px; padding-right: 8px; white-space: nowrap; }
  .feature .txt.blue { color: var(--brand); }
  .feature .txt.grey { color: #6c6c6c; }
  .feature .txt.dark { color: #4d4d4d; }

  /* Services */
  .services-bg {
    left: 0; top: 1160px; width: 1200px; height: 580px;
    background: linear-gradient(180deg, #ffffff 0%, #e5f6fb 35%, #e5f6fb 70%, #ffffff 100%);
  }
  .svc { width: 268px; text-align: center; }
  .svc .photo { width: 268px; height: 165px; box-shadow: 2px 3px 8px rgba(0,0,0,0.25); border: 4px solid #fff; }
  .svc h3 { margin-top: 16px; font-size: 20px; font-weight: 700; color: var(--ink); }
  .svc p { margin-top: 6px; font-size: 15px; line-height: 20px; color: var(--muted); padding: 0 12px; }
  .svc .btn { width: 96px; height: 34px; font-size: 16px; font-weight: 400; margin: 20px auto 0; }

  /* Clients */
  .client { width: 330px; }
  .client .logo { width: 77px; height: 77px; border-radius: 50%; background: #2b2b2b; }
  .client .who { left: 91px; top: 10px; }
  .client .who b { display: block; font-size: 19px; font-weight: 600; color: var(--brand); }
  .client .who span { display: block; font-size: 15px; color: var(--ink); margin-top: 6px; }
  .bubble {
    width: 316px; height: 129px; background: var(--panel); border-radius: 28px;
    box-shadow: 3px 5px 10px rgba(0,0,0,0.13);
    display: flex; align-items: center; justify-content: center; text-align: center;
    font-size: 14px; line-height: 20px; color: #333; padding: 0 22px;
  }
  .bubble::before {
    content: ""; position: absolute; left: 80px; top: -28px;
    border-right: 30px solid transparent; border-bottom: 30px solid var(--panel);
  }
  .bubble q { quotes: "\201C" "\201D"; }
  .bubble q::before, .bubble q::after { font-size: 28px; color: #555; vertical-align: -8px; font-weight: 700; margin: 0 3px; }

  /* Footer */
  .footer-bg { left: 0; top: 2150px; width: 1200px; height: 317px; background: linear-gradient(180deg, #ffffff, #f0f3f6); }
  .f-title { font-size: 22px; font-weight: 600; color: var(--ink); letter-spacing: 0.5px; }
  .f-link { font-size: 17px; color: #333; }
  .divider { width: 1px; background: var(--line); top: 2225px; height: 205px; }
  .social { top: 2285px; width: 42px; height: 42px; }
  .news-input {
    left: 353px; top: 2387px; width: 138px; height: 31px; background: #fff; border: 1px solid #d0d0d0;
    font-size: 13px; color: #aaa; padding-left: 8px; display: flex; align-items: center;
  }
  .subscribe {
    left: 491px; top: 2387px; width: 89px; height: 31px; background: var(--brand-deep);
    color: #fff; font-size: 13px; font-weight: 700; display: flex; align-items: center; justify-content: center;
  }
  .contact-row { display: flex; align-items: center; gap: 16px; font-size: 15px; color: #222; letter-spacing: 0.4px; }
  .map { left: 895px; top: 2256px; width: 171px; height: 117px; background: linear-gradient(135deg, #e3e6dc, #cfd6cc); box-shadow: 2px 3px 6px rgba(0,0,0,0.2); }
  .legal {
    left: 0; top: 2467px; width: 1200px; height: 90px; background: var(--brand-deep);
    color: #fff; font-size: 20px; display: flex; align-items: center; justify-content: center;
  }
</style>
</head>
<body>

<header>
  <div class="abs brand">
    <div class="brand-mark"></div>
    <div class="brand-name">Halvern Keyworks LLC</div>
  </div>
  <div class="abs home-btn">
    <svg width="24" height="22" viewBox="0 0 24 22"><path d="M12 1 L1 11 H4 V21 H10 V14 H14 V21 H20 V11 H23 Z" fill="#12b5dc"/></svg>
    Home
  </div>
  <div class="abs search">
    <span>search</span>
    <div class="go"><svg width="22" height="22" viewBox="0 0 22 22"><circle cx="9" cy="9" r="6.5" stroke="#fff" stroke-width="2.5" fill="none"/><line x1="14" y1="14" x2="20" y2="20" stroke="#fff" stroke-width="3"/></svg></div>
  </div>
  <nav class="abs nav">
    <a class="nav-item" style="left:489px;">About Us</a>
    <a class="nav-item" style="left:604px;">Services</a>
    <a class="nav-item" style="left:708px;">Locksmith services</a>
    <a class="nav-item" style="left:910px;">Price list</a>
    <a class="nav-item" style="left:1018px;">Contact</a>
  </nav>
</header>

<section class="abs hero">
  <div class="abs hero-art" role="img" aria-label="Illustration of a car key with a black head and gold blade on a key ring"></div>
  <h1 class="abs hero-copy"><span class="accent">HALVERN KEYWORKS</span> provide<br>recovery services and automotive lock-<br>smith services to the Dallas Ft-Worth<br>Area.</h1>
  <div class="abs hero-cta">Learn more</div>
  <div class="abs dots"><i class="on"></i><i></i><i></i><i></i></div>
</section>

<section>
  <div class="abs sec-head" style="left:111px;top:745px;">
    <div class="badge"><svg width="44" height="44" viewBox="0 0 44 44"><circle cx="22" cy="19" r="10" fill="#111"/><rect x="17" y="29" width="10" height="8" fill="#111"/><g stroke="#111" stroke-width="3"><line x1="22" y1="2" x2="22" y2="6"/><line x1="5" y1="19" x2="9" y2="19"/><line x1="35" y1="19" x2="39" y2="19"/><line x1="10" y1="7" x2="13" y2="10"/><line x1="34" y1="7" x2="31" y2="10"/></g></svg></div>
    <div class="label">About Us</div>
  </div>
  <p class="abs about-text">We are a locally owned company with over 6 years of experience in the automotive industry. We provide recovery services and automotive locksmith services to the Dallas Ft-Worth Area.Our main goal is to provide unmatched customer service both to the client and your customer. You will appreciate the value of our professional approach to all your automotive needs. Our experienced staff will always be eager to assist you. We look forward to being your reliable business partner when your repos-session or locksmith needs arise</p>
  <div class="abs btn read-more">Read more</div>

  <div class="abs feature" style="top:747px;">
    <div class="ico"><svg width="84" height="66" viewBox="0 0 90 70"><rect x="4" y="24" width="46" height="30" rx="3" fill="#12b5dc"/><path d="M50 32 H64 L74 44 V54 H50 Z" fill="#12b5dc"/><circle cx="18" cy="58" r="7" fill="#12b5dc" stroke="#fff" stroke-width="2"/><circle cx="62" cy="58" r="7" fill="#12b5dc" stroke="#fff" stroke-width="2"/><circle cx="66" cy="20" r="17" fill="#fff" stroke="#12b5dc" stroke-width="4"/><path d="M66 10 V20 H74" stroke="#12b5dc" stroke-width="3" fill="none"/></svg></div>
    <div class="txt blue">Free Delivery<br>Of Product</div>
  </div>
  <div class="abs feature" style="top:878px;">
    <div class="ico"><svg width="64" height="64" viewBox="0 0 70 70"><path d="M10 26 L35 14 L60 26 V60 H10 Z" fill="none" stroke="#4d5a61" stroke-width="6"/><rect x="24" y="34" width="22" height="26" fill="#4d5a61"/></svg></div>
    <div class="txt grey">Free Storage<br>Facility</div>
  </div>
  <div class="abs feature" style="top:1009px;">
    <div class="ico"><svg width="72" height="64" viewBox="0 0 80 70"><path d="M14 12 C8 14 6 22 10 32 C16 46 28 58 42 64 C50 67 56 64 58 58 L50 48 L42 52 C34 48 26 40 22 32 L26 24 Z" fill="#4d5a61"/><ellipse cx="54" cy="18" rx="18" ry="14" fill="#12b5dc"/><circle cx="46" cy="18" r="2.5" fill="#fff"/><circle cx="54" cy="18" r="2.5" fill="#fff"/><circle cx="62" cy="18" r="2.5" fill="#fff"/></svg></div>
    <div class="txt dark">24X7<br>Customer Care</div>
  </div>
</section>

<section>
  <div class="abs services-bg"></div>
  <div class="abs sec-head" style="left:111px;top:1176px;">
    <div class="badge"><svg width="52" height="52" viewBox="0 0 52 52"><circle cx="18" cy="32" r="12" fill="none" stroke="#111" stroke-width="8" stroke-dasharray="5 4"/><circle cx="18" cy="32" r="5" fill="#111"/><circle cx="38" cy="14" r="8" fill="none" stroke="#111" stroke-width="6" stroke-dasharray="4 3"/></svg></div>
    <div class="label">Our Services</div>
  </div>

  <article class="abs svc" style="left:133px;top:1323px;">
    <div class="photo" role="img" aria-label="Photo of a tow truck with a crane lifting a white van" style="background:linear-gradient(180deg,#f4f6f8 0%,#e7ebef 55%,#9aa6b0 100%);"></div>
    <h3>Towing Services</h3>
    <p>Lorem Ipsum is simply dummy text of the printing and typeset-ting industry. Lorem Ipsum has been the industry's standard</p>
    <div class="btn">Click Here</div>
  </article>
  <article class="abs svc" style="left:469px;top:1323px;">
    <div class="photo" role="img" aria-label="Photo of a car carrier truck loaded with vehicles" style="background:linear-gradient(180deg,#aab9cf 0%,#c9d2dc 45%,#8a6a6f 80%,#6b4a4c 100%);"></div>
    <h3>Vehicle Transportation</h3>
    <p>Lorem Ipsum is simply dummy text of the printing and typeset-ting industry. Lorem Ipsum has been the industry's standard</p>
    <div class="btn">Click Here</div>
  </article>
  <article class="abs svc" style="left:810px;top:1323px;">
    <div class="photo" role="img" aria-label="Illustration of a padlock shaped like a blue globe" style="background:linear-gradient(180deg,#ffffff 0%,#d6e9f6 50%,#8fc0e6 100%);"></div>
    <h3>Locksmith Services</h3>
    <p>Lorem Ipsum is simply dummy text of the printing and typeset-ting industry. Lorem Ipsum has been the industry's standard</p>
    <div class="btn">Click Here</div>
  </article>
</section>

<section>
  <div class="abs sec-head" style="left:111px;top:1773px;">
    <div class="badge"><svg width="48" height="48" viewBox="0 0 48 48"><circle cx="22" cy="13" r="10" fill="#111"/><path d="M4 44 C4 30 12 25 22 25 C30 25 36 29 38 36 L30 44 Z" fill="#111"/><path d="M32 44 L44 30 L47 33 L35 46 Z" fill="#111"/></svg></div>
    <div class="label">Our Clients Say's</div>
  </div>

  <div class="abs client" style="left:170px;top:1887px;">
    <div class="logo"></div>
    <div class="abs who"><b>QRT portal</b><span>Nov 10,2014</span></div>
  </div>
  <div class="abs bubble" style="left:176px;top:1978px;"><q>Lorem Ipsum is simply dummy text of the printing and typesetting</q></div>

  <div class="abs client" style="left:652px;top:1887px;">
    <div class="logo"></div>
    <div class="abs who"><b>QRT portal</b><span>Nov 10,2014</span></div>
  </div>
  <div class="abs bubble" style="left:658px;top:1978px;"><q>Lorem Ipsum is simply dummy text of the printing and typesetting</q></div>
</section>

<footer>
  <div class="abs footer-bg"></div>

  <div class="abs f-title" style="left:136px;top:2232px;">Quick Links</div>
  <div class="abs f-link" style="left:143px;top:2286px;">Home</div>
  <div class="abs f-link" style="left:143px;top:2324px;">Services</div>
  <div class="abs f-link" style="left:143px;top:2361px;">Locksmith</div>
  <div class="abs f-link" style="left:143px;top:2399px;">Price List</div>

  <div class="abs divider" style="left:303px;"></div>

  <div class="abs f-title" style="left:355px;top:2232px;">Fallow Us On</div>
  <div class="abs social" style="left:353px;background:#2fa9e1;" role="img" aria-label="Social network link"></div>
  <div class="abs social" style="left:406px;background:#d8322a;" role="img" aria-label="Video channel link"></div>
  <div class="abs social" style="left:459px;background:#3b5a98;" role="img" aria-label="Social network link"></div>
  <div class="abs social" style="left:512px;background:#1b7eb6;" role="img" aria-label="Professional network link"></div>
  <div class="abs f-title" style="left:353px;top:2346px;">News Letter</div>
  <div class="abs news-input">Your E-mail</div>
  <div class="abs subscribe">SUBSCRIBE</div>

  <div class="abs divider" style="left:617px;"></div>

  <div class="abs f-title" style="left:660px;top:2232px;">Contact Us</div>
  <div class="abs contact-row" style="left:655px;top:2290px;">
    <svg width="14" height="20" viewBox="0 0 14 20"><path d="M7 0 C3 0 0 3 0 7 C0 12 7 20 7 20 C7 20 14 12 14 7 C14 3 11 0 7 0 Z" fill="#111"/><circle cx="7" cy="7" r="2.5" fill="#fff"/></svg>
    <span>410 CORVANE AVE</span>
  </div>
  <div class="abs contact-row" style="left:685px;top:2319px;"><span>DALLAS, TX 75209</span></div>
  <div class="abs contact-row" style="left:655px;top:2355px;">
    <svg width="16" height="16" viewBox="0 0 16 16"><path d="M3 1 C1 2 0 4 2 8 C4 12 8 15 12 15 C14 15 15 13 15 12 L12 9 L10 11 C8 10 6 8 5 6 L7 4 Z" fill="#111"/></svg>
    <span>+888-555-0142</span>
  </div>
  <div class="abs contact-row" style="left:655px;top:2394px;">
    <svg width="18" height="14" viewBox="0 0 18 14"><rect x="1" y="1" width="16" height="12" fill="none" stroke="#111" stroke-width="2"/><path d="M1 1 L9 8 L17 1" fill="none" stroke="#111" stroke-width="2"/></svg>
    <span>contact@halvernkeyworks.example</span>
  </div>
  <div class="abs map" role="img" aria-label="Street map showing the office location"></div>

  <div class="abs legal">All Rights Reserved@ 2014 contact@halvernkeyworks.example</div>
</footer>

</body>
</html>
```